Stylish Business Card for Modern hair salon

I need a simple business card design using our salon logo and colours that are in the logo. We service clients of all ages but predominantly those in the 18 to 55 age range. We have a young staff and are looking to have a card that will present a modern and clean image that represents who we are. The card should be in black and white same as our logo. Minimal use of other colours is allowed.

Industry/Entity Type

Hair And Beauty

Contact Information for Business Card

The design should have the following information
salon name - TR Hair Studio
address - 2751 Birchfield Rd.E. Mississauga, ON L7P3K2
phone - 905 614-2870
website - trhairexample.ca
instagram - tr.hairstudio
twitter - @TR_HairStudio

Colors
000000
ffffff
474747

Requirements
Must have
• simple design, salon name, address, phone, website, instagram, twitter info
• Back of card should have the following:
• YOUR NEXT APPOINTMENT
• DATE
• TIME
Nice to have
• simple design, clear to see and read,
• predominantly black and white colour, minimal use of other colours is ok
Should not have
• many colours, various fonts

```html
<!DOCTYPE html>
<html lang="en">
<head>
<meta charset="utf-8">
<title>TR Hair Studio – Business Card</title>
<link href="https://fonts.googleapis.com/css2?family=Federo&family=Josefin+Sans:wght@600&family=Roboto:wght@400&display=swap" rel="stylesheet">
<style>
  :root {
    --black: #0b0b0c;
    --white: #ffffff;
    --paper: #f4f4f4;
    --grey: #474747;
    --backdrop: #e4e4e4;
    --line: #111111;
  }
  * { margin: 0; padding: 0; box-sizing: border-box; }
  html, body { width: 1200px; height: 576px; overflow: hidden; }
  body { background: var(--backdrop); position: relative; font-family: "Roboto", Arial, sans-serif; }

  .card {
    position: absolute;
    top: 138px;
    width: 484px;
    height: 293px;
    border-radius: 14px;
    background: var(--black);
    overflow: hidden;
    color: var(--white);
  }
  .card--back { left: 82px; }
  .card--front { left: 602px; }

  /* Appointment side */
  .appointment-title {
    position: absolute;
    left: 20px; top: 40px;
    font-family: "Josefin Sans", Arial, sans-serif;
    font-weight: 600;
    font-size: 16.5px;
    line-height: 21px;
    letter-spacing: 1.6px;
  }
  .brand-name {
    font-family: "Federo", Georgia, serif;
    font-weight: 400;
    white-space: nowrap;
  }
  .card--back .brand-name {
    position: absolute;
    right: 22px; top: 40px;
    font-size: 36px;
    color: var(--white);
  }
  .appointment-form {
    position: absolute;
    left: 18px; top: 116px;
    width: 447px; height: 112px;
    background: var(--paper);
    color: var(--line);
    font-family: "Josefin Sans", Arial, sans-serif;
    font-weight: 600;
    font-size: 13px;
    letter-spacing: 1.2px;
  }
  .form-row { position: absolute; left: 19px; right: 19px; display: flex; align-items: flex-end; gap: 6px; }
  .form-row--name { top: 26px; }
  .form-row--extra { top: 62px; }
  .form-row--when { top: 82px; }
  .fill-line { flex: 1; border-bottom: 2px solid var(--line); height: 13px; }
  .fill-line--time { flex: 0 0 75px; }
  .cancel-note {
    position: absolute;
    left: 0; right: 0; top: 246px;
    text-align: center;
    font-size: 13px;
    line-height: 17px;
  }

  /* Contact side */
  .curve-art { position: absolute; inset: 0; }
  .studio-name {
    position: absolute;
    left: 28px; top: 26px;
    font-family: "Federo", Georgia, serif;
    font-size: 21px;
    letter-spacing: 0.3px;
  }
  .contact-list, .social-list {
    position: absolute;
    left: 28px;
    list-style: none;
    font-size: 12px;
    line-height: 16px;
  }
  .contact-list { top: 60px; }
  .social-list { top: 322px; top: 184px; }
  .contact-list li, .social-list li { display: flex; gap: 9px; align-items: flex-start; }
  .icon { width: 12px; height: 12px; flex: 0 0 12px; margin-top: 2px; fill: var(--white); }
  .social-list li { margin-bottom: 2px; }
  .social-dot { width: 11px; height: 11px; border-radius: 50%; background: var(--grey); flex: 0 0 11px; margin: 2px 1px 0 0; }
  .card--front .brand-name {
    position: absolute;
    left: 300px; width: 170px; top: 118px;
    text-align: center;
    font-size: 42px;
    color: var(--black);
  }
</style>
</head>
<body>

<section class="card card--back" aria-label="Appointment card">
  <h2 class="appointment-title">YOUR NEXT<br>APPOINTMENT</h2>
  <div class="brand-name">TR Hair</div>
  <div class="appointment-form">
    <div class="form-row form-row--name"><span>NAME</span><span class="fill-line"></span></div>
    <div class="form-row form-row--extra"><span class="fill-line"></span></div>
    <div class="form-row form-row--when"><span>DATE</span><span class="fill-line"></span><span>TIME</span><span class="fill-line fill-line--time"></span></div>
  </div>
  <p class="cancel-note">If you are unable to keep your appointment,<br>provide at least 2 business days notice or full visit fees apply.</p>
</section>

<section class="card card--front" aria-label="Contact card">
  <svg class="curve-art" width="484" height="293" viewBox="0 0 484 293" aria-hidden="true">
    <path d="M316 0 C250 70 242 200 302 293 L484 293 L484 0 Z" fill="var(--paper)"/>
    <path d="M302 0 C262 40 246 112 262 182 C258 112 274 44 312 0 Z" fill="var(--grey)"/>
  </svg>
  <h1 class="studio-name">TR Hair Studio</h1>
  <ul class="contact-list">
    <li><svg class="icon" viewBox="0 0 24 24"><path d="M6.6 10.8a15.1 15.1 0 0 0 6.6 6.6l2.2-2.2c.3-.3.7-.4 1-.2 1.1.4 2.3.6 3.6.6.6 0 1 .4 1 1V20c0 .6-.4 1-1 1A17 17 0 0 1 3 4c0-.6.4-1 1-1h3.5c.6 0 1 .4 1 1 0 1.3.2 2.5.6 3.6.1.3 0 .7-.2 1z"/></svg>905 614-2870</li>
    <li><svg class="icon" viewBox="0 0 24 24"><circle cx="12" cy="12" r="9.5" fill="none" stroke="#fff" stroke-width="2"/><path d="M2.5 12h19M12 2.5c3 3 3 16 0 19M12 2.5c-3 3-3 16 0 19" fill="none" stroke="#fff" stroke-width="1.6"/></svg>www.trhairexample.ca</li>
    <li><svg class="icon" viewBox="0 0 24 24"><path d="M12 2a7 7 0 0 0-7 7c0 5.2 7 13 7 13s7-7.8 7-13a7 7 0 0 0-7-7zm0 9.5a2.5 2.5 0 1 1 0-5 2.5 2.5 0 0 1 0 5z"/></svg><span>2751 Birchfield Rd.E.<br>Mississauga, ON L7P3K2</span></li>
  </ul>
  <ul class="social-list">
    <li><span class="social-dot"></span>tr.hairstudio</li>
    <li><span class="social-dot"></span>@TR_HairStudio</li>
  </ul>
  <div class="brand-name">TR Hair</div>
</section>

</body>
</html>
```